Brightwell Giving Inc

We need a full re-design of our non-profit organization website (www.brightwellgiving.org). Ideally, we are looking to make it more attractive, user-friendly, and interactive with our business model.

Please make sure to user colors that ago with our logo.

We need a homepage done and we also need a content page done where we will use for the other pages to fill with content.

Target Market(s)

Clothes/textiles donations.

Industry/Entity Type

Charity

Number of Pages Required

2 page

Colors

Designer to choose colors to be used in the design.

Requirements
Must have
• It must match the styling of our logo and same colors as current website. (www.brightwellgiving.org)
Nice to have
• Sleek homepage that is easy to understand and get our main points across.

```html
<!DOCTYPE html>
<html lang="en">
<head>
<meta charset="utf-8">
<title>Brightwell Giving — Home</title>
<link href="https://fonts.googleapis.com/css2?family=Noto+Serif:wght@700&family=Roboto+Condensed:wght@400;700&display=swap" rel="stylesheet">
<style>
:root{
  --green:#3e7320;
  --green-dark:#2f5a17;
  --green-light:#6dbb45;
  --yellow:#f7c600;
  --ink:#1f1f1f;
  --grey:#8a8a8a;
  --nav-bg:#f1f1f1;
  --footer-bg:#2a2a2a;
  --white:#ffffff;
  --serif:"Noto Serif", Georgia, serif;
  --sans:"Roboto Condensed", Arial, sans-serif;
}
*{box-sizing:border-box;margin:0;padding:0}
html,body{width:1200px;height:2326px;overflow:hidden}
body{font-family:var(--sans);color:var(--ink);background:var(--white)}
.wrap{width:878px;margin:0 auto;position:relative}

/* Hero */
.hero{position:relative;height:496px;background:linear-gradient(100deg,#5a4a3a 0%,#8a7560 40%,#6f6a66 70%,#4a4d55 100%)}
.hero-photo{position:absolute;inset:0}
.hero .wrap{height:100%}
.brand{position:absolute;top:32px;left:0;display:flex;align-items:center;gap:8px}
.brand-dot{width:34px;height:34px;background:var(--yellow);border-radius:50%}
.brand-name{font-family:var(--serif);font-size:18px;color:var(--yellow);line-height:1}
.brand-tag{display:block;font-family:var(--sans);font-size:12px;color:var(--white);margin-top:3px}
.hero-title{position:absolute;top:228px;left:0;font-family:var(--serif);font-size:56px;color:var(--yellow);letter-spacing:1px;line-height:1.05;padding-bottom:6px;border-bottom:2px solid var(--white)}
.hero-sub{position:absolute;top:308px;left:0;color:var(--white);font-weight:700;font-size:14px}

/* Nav */
.nav{height:44px;background:var(--nav-bg)}
.nav .wrap{height:100%;display:flex;align-items:center}
.nav-links{display:flex;gap:24px;list-style:none;font-weight:700;font-size:13px}
.social{display:flex;gap:14px;margin-left:40px}
.social span{width:13px;height:13px;border-radius:50%;background:#3aa8d8;opacity:.75}
.nav-donate{margin-left:auto;height:44px;width:121px;background:#1e1e1e;color:var(--white);font-weight:700;font-size:12px;display:flex;align-items:center;justify-content:center;gap:10px;margin-right:0}
.nav-donate svg{width:28px;height:26px}

/* Section titles */
.section-title{font-family:var(--serif);font-size:34px;text-align:center;display:inline-block;padding-bottom:6px;border-bottom:2px solid currentColor}
.center{text-align:center}

/* Welcome */
.welcome{height:261px;background:var(--green);color:var(--white);padding-top:50px}
.welcome .section-title{border-color:var(--white)}
.welcome p{width:800px;margin:26px auto 0;font-size:12.5px;line-height:18.5px;text-align:center}

/* How it works */
.how{height:476px;padding-top:54px}
.how .section-title{font-size:32px;border-bottom-width:1.5px}
.steps{display:flex;justify-content:space-between;margin-top:48px;padding:0 25px}
.step{width:264px;text-align:center}
.step-art{width:136px;height:124px;margin:0 auto;background:linear-gradient(135deg,var(--green-light),var(--yellow) 55%,var(--green));border-radius:6px}
.step h3{font-size:16px;line-height:19px;margin-top:35px;font-weight:700}
.step h3.accent{color:var(--green)}
.step p{font-size:13px;line-height:17px;color:var(--grey);margin-top:20px}

/* Mission */
.mission{position:relative;height:382px;background:linear-gradient(90deg,#3a2e26 0%,#5a4636 45%,#4a3a30 100%);color:var(--white);padding-top:58px}
.mission-photo{position:absolute;inset:0}
.mission .inner{position:relative}
.mission .section-title{font-size:32px;border-color:var(--white)}
.mission p{width:780px;margin:26px auto 0;font-size:12.5px;line-height:18.5px;text-align:center}
.btn{display:inline-block;background:var(--yellow);color:var(--ink);font-weight:700;font-size:13px;width:122px;height:45px;line-height:45px;text-align:center;margin-top:56px}

/* Donate */
.donate{height:406px;padding-top:60px}
.donate h2{font-family:var(--serif);font-size:35px;line-height:1}
.cards{display:flex;gap:31px;margin-top:20px}
.card{width:196px}
.card-head{border-top:3px solid var(--green-dark);border-bottom:1.5px solid var(--green-dark);height:67px;display:flex;align-items:center;gap:12px}
.card-mark{width:30px;height:24px;background:var(--yellow);border:2px solid var(--green-dark)}
.card-title{color:var(--green);font-weight:700;font-size:15px}
.bar{height:11px;background:#222;margin-top:22px;border-radius:2px;overflow:hidden}
.bar span{display:block;height:100%;width:78%;background:var(--green-light)}
.bar-labels{display:flex;justify-content:space-between;margin-top:6px;font-weight:700;font-size:13px;line-height:1}
.bar-labels small{display:block;font-size:8px;margin-top:2px}
.bar-labels div:last-child{text-align:right}
.meta{font-size:12.5px;color:#666;margin-top:18px;line-height:17px}
.meta b{color:var(--ink);font-weight:400}
.summary{font-size:11.5px;color:var(--grey);line-height:15px;margin-top:12px}

/* Footer */
.footer{height:261px;background:var(--footer-bg);color:#aaa;padding-top:35px}
.footer .wrap{display:flex}
.footer-about{width:386px}
.badges{display:flex;gap:10px;align-items:center}
.badge{width:52px;height:56px;background:#f2e15a;border-radius:3px}
.badge.round{width:60px;height:60px;border-radius:50%;background:#e0b41c}
.footer-about p{font-size:11px;line-height:16px;margin-top:32px}
.copyright{font-size:11px;margin-top:22px}
.footer-col{border-left:2px solid var(--green-light);padding-left:15px;height:160px}
.footer-links{list-style:none;width:223px;font-size:11px;font-weight:700;color:var(--green-light);line-height:21px;margin-top:-4px}
.footer-connect{width:269px;font-size:11.5px;font-weight:700;color:var(--green-light)}
.footer-connect .label{display:block}
.footer-connect .sub{margin-top:50px}
.email{margin-top:10px;height:30px;border:1.5px solid var(--green-light);background:#111;color:#bbb;font-style:italic;font-weight:400;font-size:10.5px;padding:0 8px;line-height:27px;width:225px}
.submit{width:225px;height:28px;background:var(--green-light);color:var(--white);text-align:center;line-height:28px;font-size:11px}
</style>
</head>
<body>

<header class="hero">
  <div class="hero-photo" role="img" aria-label="Photo of volunteers sorting donated clothes over a donations box in a warehouse"></div>
  <div class="wrap">
    <div class="brand">
      <span class="brand-dot"></span>
      <div><span class="brand-name">BRIGHTWELL GIVING</span><span class="brand-tag">Think Globally while Donating Locally</span></div>
    </div>
    <h1 class="hero-title">BRIGHTWELL GIVING</h1>
    <p class="hero-sub">Think Globally While Donating Locally</p>
  </div>
</header>

<nav class="nav">
  <div class="wrap">
    <ul class="nav-links">
      <li>HOME</li><li>MISSIONS</li><li>HOW IT WORKS</li><li>ABOUT US</li><li>SPONSORS</li><li>NEWS</li><li>DONATE</li><li>WALL OF NEEDS</li>
    </ul>
    <div class="social" aria-hidden="true"><span></span><span></span><span></span></div>
    <div class="nav-donate">DONATE
      <svg viewBox="0 0 28 26" fill="none" stroke="#fff" stroke-width="1.4"><path d="M14 12c-3-2.5-5-4-5-6a2.5 2.5 0 0 1 5-1 2.5 2.5 0 0 1 5 1c0 2-2 3.5-5 6z"/><path d="M2 14c3 0 5 2 8 5h8c2 0 3-1 3-1l5-5"/></svg>
    </div>
  </div>
</nav>

<section class="welcome center">
  <h2 class="section-title">WELCOME TO THE BRIGHTWELL GIVING</h2>
  <p>Brightwell Giving is a non-profit organization that was created for one purpose: helping the less fortunate in our country's time of greatest need. Started in 2007, Brightwell Giving has been a dedicated member of its local communities over the past four years. The company's clothing collection efforts have allowed it to provide some of the neediest members of the community to clothe themselves and their families. The company's goal is to ensure that some of the most basic needs of the community's members are met thru the philanthropic efforts of the organizations members and contributors.</p>
</section>

<section class="how">
  <div class="wrap">
    <div class="center"><h2 class="section-title">HOW IT WORKS</h2></div>
    <div class="steps">
      <div class="step">
        <div class="step-art" role="img" aria-label="Illustration of a shirt with a clothing basket"></div>
        <h3 class="accent">Drop off clothing at your closest donation bin.</h3>
        <p>We have different collection procedures. For outdoors we can place a donation bin, a metal container about 48"L X 48"WX66"H.</p>
      </div>
      <div class="step">
        <div class="step-art" role="img" aria-label="Illustration of a shirt with a person carrying a bundle"></div>
        <h3>We pick it up and take it to our sorting facility</h3>
        <p>We have different collection procedures. For outdoors we can place a donation bin, a metal container about 48"L X 48"WX66"H.</p>
      </div>
      <div class="step">
        <div class="step-art" role="img" aria-label="Illustration of a shirt with a heart"></div>
        <h3>Charities get clothing. We pay you for the clothes.</h3>
        <p>We have different collection procedures. For outdoors we can place a donation bin, a metal container about 48"L X 48"WX66"H.</p>
      </div>
    </div>
  </div>
</section>

<section class="mission center">
  <div class="mission-photo" role="img" aria-label="Dimmed photo of children leaning on a wooden table"></div>
  <div class="inner">
    <h2 class="section-title">MISSION STATEMENT</h2>
    <p>Brightwell Giving has a two part mission to help local communities while helping the planet. The average American discards 68 lbs of clothing annually. That is 1,325,340,196 lbs for New York State alone and 21,202,400,000 lbs for the U.S. every year! By keeping unwanted clothes out of the trash can we are greatly reducing the amount of material that enters our landfills. We are also turning the unwanted clothes into funding for our local communities. We are asking for your help to increase local support. Simply put, there is no better time to act than now.</p>
    <span class="btn">LEARN MORE</span>
  </div>
</section>

<section class="donate">
  <div class="wrap">
    <h2>DONATE</h2>
    <div class="cards">
      <article class="card">
        <div class="card-head"><span class="card-mark"></span><span class="card-title">NORTHFIELD LETTER</span></div>
        <div class="bar"><span></span></div>
        <div class="bar-labels"><div>$10,000<small>START</small></div><div>$25,000<small>END</small></div></div>
        <p class="meta">June 4, 2016 Categories :<br><b>MAIN</b> by <b>ADMIN</b></p>
        <p class="summary">May 25, 2015: Donated clothes to Northfield Employee Service Team of NY.</p>
      </article>
      <article class="card">
        <div class="card-head"><span class="card-mark"></span><span class="card-title">NORTHFIELD LETTER</span></div>
        <div class="bar"><span></span></div>
        <div class="bar-labels"><div>$10,000<small>START</small></div><div>$25,000<small>END</small></div></div>
        <p class="meta">June 4, 2016 Categories :<br><b>MAIN</b> by <b>ADMIN</b></p>
        <p class="summary">May 25, 2015: Donated clothes to Northfield Employee Service Team of NY.</p>
      </article>
      <article class="card">
        <div class="card-head"><span class="card-mark"></span><span class="card-title">NORTHFIELD LETTER</span></div>
        <div class="bar"><span></span></div>
        <div class="bar-labels"><div>$10,000<small>START</small></div><div>$25,000<small>END</small></div></div>
        <p class="meta">June 4, 2016 Categories :<br><b>MAIN</b> by <b>ADMIN</b></p>
        <p class="summary">May 25, 2015: Donated clothes to Northfield Employee Service Team of NY.</p>
      </article>
      <article class="card">
        <div class="card-head"><span class="card-mark"></span><span class="card-title">NORTHFIELD LETTER</span></div>
        <div class="bar"><span></span></div>
        <div class="bar-labels"><div>$10,000<small>START</small></div><div>$25,000<small>END</small></div></div>
        <p class="meta">June 4, 2016 Categories :<br><b>MAIN</b> by <b>ADMIN</b></p>
        <p class="summary">May 25, 2015: Donated clothes to Northfield Employee Service Team of NY.</p>
      </article>
    </div>
  </div>
</section>

<footer class="footer">
  <div class="wrap">
    <div class="footer-about">
      <div class="badges" aria-hidden="true"><span class="badge"></span><span class="badge"></span><span class="badge"></span><span class="badge round"></span></div>
      <p>Lorem Ipsum Dolor Sit Amet<br>Consectetur Amet Lorem<br>(555) 014-2290<br>info@brightwellgiving.org</p>
      <p class="copyright">© Copyright 2018 Brightwell Giving, All Rights Reserved.</p>
    </div>
    <div class="footer-col">
      <ul class="footer-links">
        <li>HOME</li><li>MISSIONS</li><li>HOW IT WORKS</li><li>ABOUT US</li><li>SPONSORS</li><li>NEWS</li><li>DONATE</li><li>WALL OF NEEDS</li>
      </ul>
    </div>
    <div class="footer-col footer-connect">
      <span class="label">CONNECT</span>
      <span class="label sub">SUBSCRIBE</span>
      <div class="email">Enter Your Email</div>
      <div class="submit">SUBMIT</div>
    </div>
  </div>
</footer>

</body>
</html>
```